Business card design needed for elearning/LMS consultant

I'm an elearning and learning management system (LMS) consultant that requires a minimalist, technology/cutting edge, business card. I do not have a logo or colour scheme. I offer clients hands on expertise in 'elearning authouring', 'LMS ecosystems', 'elearning strategy', 'technical implementation', 'mlearning', 'LMS evaluation', 'big data', 'learner analytics' and 'reporting strategy', 'social learning', 'elearning blueprint'. I'm thinking a 'tag cloud' of the above services on the back of the card, with contact details on front, but unsure if it's passe so please don't let it constrain you.

Target Market(s)

C-level executives, learning and development senior management,

Industry/Entity Type

Business

Contact Information for Business Card

Owen Haldric
owen.haldric@mailvane.net
0412 836 197

Requirements
Should not have
• cheesy headshots, overused stockphotos, CLIPART and comic sans ;)

```html
<!DOCTYPE html>
<html lang="en">
<head>
<meta charset="utf-8">
<title>Owen Haldric – Business Card</title>
<link rel="stylesheet" href="https://fonts.googleapis.com/css2?family=Exo+2:wght@600;700&family=Jura:wght@500;600&family=Arimo:wght@400;700&display=swap">
<style>
  :root {
    --page: #ffffff;
    --back-card: #4a4746;
    --back-band: #1e1c1c;
    --art-tone: #524f4e;
    --art-edge: #4d4a49;
    --front-light: #ffffff;
    --front-edge: #dcdcdc;
    --brand-blue: #1b8fd8;
    --muted-grey: #5a5a5a;
  }
  html, body {
    margin: 0;
    padding: 0;
    width: 1200px;
    height: 741px;
    overflow: hidden;
    background: var(--page);
  }
  .canvas {
    position: relative;
    width: 1200px;
    height: 741px;
  }
  .card {
    position: absolute;
    top: 231px;
    width: 524px;
    height: 284px;
    overflow: hidden;
  }
  .card--back {
    left: 69px;
    background: var(--back-card);
  }
  .card--front {
    left: 619px;
    background: radial-gradient(ellipse 70% 80% at 50% 30%, var(--front-light) 0%, #f0f0f0 50%, var(--front-edge) 100%);
  }
  .brand-band {
    position: absolute;
    left: 0;
    top: 14px;
    width: 175px;
    height: 46px;
    background: linear-gradient(90deg, var(--back-band) 0%, var(--back-band) 45%, rgba(30,28,28,0) 100%);
  }
  .brand-name {
    position: absolute;
    font-family: "Exo 2", sans-serif;
    font-weight: 700;
    font-size: 24px;
    letter-spacing: 0.5px;
    color: var(--brand-blue);
    line-height: 1;
  }
  .card--back .brand-name { left: 26px; top: 24px; }
  .card--front .brand-name { left: 22px; top: 25px; }
  .back-art {
    position: absolute;
    left: 131px;
    top: 92px;
    width: 260px;
    height: 148px;
    background: radial-gradient(ellipse 60% 70% at 50% 55%, var(--art-tone) 0%, var(--art-edge) 100%);
  }
  .contact {
    position: absolute;
    left: 0;
    right: 0;
    top: 96px;
    text-align: center;
  }
  .contact__name {
    margin: 0;
    font-family: "Exo 2", sans-serif;
    font-weight: 600;
    font-size: 39px;
    line-height: 1;
    color: var(--brand-blue);
  }
  .contact__audience {
    margin: 13px 0 0;
    font-family: "Jura", sans-serif;
    font-weight: 600;
    font-size: 20px;
    letter-spacing: 0.8px;
    line-height: 1;
    color: var(--brand-blue);
  }
  .contact__roles {
    margin: 4px 0 0;
    font-family: "Jura", sans-serif;
    font-weight: 500;
    font-size: 13px;
    line-height: 14px;
    color: var(--muted-grey);
  }
  .contact__phone {
    margin: 14px 0 0;
    font-family: "Arimo", sans-serif;
    font-size: 15px;
    line-height: 1;
    color: var(--brand-blue);
  }
  .contact__email {
    margin: 6px 0 0;
    font-family: "Arimo", sans-serif;
    font-weight: 700;
    font-size: 13px;
    line-height: 1;
    color: var(--brand-blue);
  }
</style>
</head>
<body>
<main class="canvas">
  <section class="card card--back" aria-label="Card back">
    <div class="brand-band"></div>
    <span class="brand-name">Veltra</span>
    <div class="back-art" role="img" aria-label="Faint outline cloud illustration in soft grey"></div>
  </section>

  <section class="card card--front" aria-label="Card front">
    <span class="brand-name">Veltra</span>
    <div class="contact">
      <h1 class="contact__name">Owen Haldric</h1>
      <p class="contact__audience">C-LEVEL EXECUTIVES</p>
      <p class="contact__roles">LEARNING AND DEVELOPMENT<br>SENIOR MANAGEMENT</p>
      <p class="contact__phone">0412 836 197</p>
      <p class="contact__email">owen.haldric@mailvane.net</p>
    </div>
  </section>
</main>
</body>
</html>
```